Web application design for investigative software

ClueVane is an investigation web application that would organize, create visualizations and allow collaboration. It’s available to anyone and can be used by students, historians, watchdog groups, civic hackers, investigative reporters, mystery enthusiasts, authors, even conspiracy theorists.

We are looking for two related pages. The first, a splash, or front, page and the second a ‘template’ for the web application. They should both be styled the same. The only restriction is that the logo is set.

The design should also be modern and visually well organized — employing a combination of visual devices and info graphics. Keep it light and not too heavy but strong/ professional. Do not be influenced by the current colors of cluevane-example.com, though the colors should be compatible with the logo..

The pages should be compatible with bootstrap, mostly for it’s JS and component functionality. It can be advised by the designer that a subset of bootstrap be used.

The splash page.
Something along the lines of (though not a copy of) :
https://www.plorvex-example.com/advertise
http://www.brimtallhost-example.net/
http://www.corvilode-example.com/
http://www.fennaquist-example.com/

I have a very rough wire frame ish html file uploaded. Use a a guide, but alternate ideas are encouraged.

The application page should have some sort of bar for at the top for system level links a header and a footer. A vertical column to the left between the header and footer for ads, though this will be dynamic as a user can pay out of seeing adds. All dynamic actions will be made by the developers at ClueVane.

WARNING. Please do not submit pre-made templates from some template website. We can do that ourselves for free.

This project will deliver CODE. HTML, CSS and supporting graphics and files.

```html
<!DOCTYPE html>
<html lang="en">
<head>
<meta charset="utf-8">
<title>ClueVane — Track, Relate, Investigate, Solve</title>
<link rel="stylesheet" href="https://fonts.googleapis.com/css2?family=Roboto+Condensed:wght@400;700&family=Arimo:wght@400&display=swap">
<style>
  :root {
    --red: #d8291a;
    --ink: #2b2b2b;
    --nav: #555555;
    --white: #ffffff;
    --card-dark: #676767;
    --card-light: #f1f1f1;
    --card-border: #d6d6d6;
    --muted: #666666;
    --band-grey: #e6e6e6;
    --footer: #3b3b3b;
    --footer-text: #bdbdbd;
    --caption-bg: rgba(20, 20, 20, 0.88);
  }
  * { box-sizing: border-box; margin: 0; padding: 0; }
  html, body { width: 861px; height: 1200px; overflow: hidden; background: var(--white); }
  body { font-family: "Arimo", Arial, sans-serif; color: var(--ink); position: relative; }
  .heading { font-family: "Roboto Condensed", "Arial Narrow", sans-serif; font-weight: 700; text-transform: uppercase; }

  .site-header { position: absolute; top: 0; left: 0; width: 861px; height: 58px; background: var(--white); }
  .brand { position: absolute; left: 126px; top: 12px; display: flex; align-items: center; gap: 7px; }
  .brand-dot { width: 28px; height: 28px; border-radius: 50%; background: var(--red); }
  .brand-name { font-family: "Roboto Condensed", sans-serif; font-weight: 700; font-size: 22px; color: var(--ink); }
  .main-nav { position: absolute; top: 25px; left: 587px; display: flex; gap: 19px; font-size: 8.5px; color: var(--nav); }
  .main-nav .caret::after { content: ""; display: inline-block; margin-left: 5px; vertical-align: 1px; border-left: 3px solid transparent; border-right: 3px solid transparent; border-top: 3px solid var(--nav); }

  .hero { position: absolute; top: 58px; left: 0; width: 861px; height: 305px; background: linear-gradient(100deg, #cfcfcf 0%, #7a7a7a 35%, #4a4a4a 55%, #8c8c8c 80%, #b5b5b5 100%); }
  .hero-caption { position: absolute; left: 475px; height: 31px; padding: 0 14px; background: var(--caption-bg); color: var(--white); font-size: 11.5px; line-height: 31px; white-space: nowrap; }
  .hero-caption.one { top: 156px; }
  .hero-caption.two { top: 195px; }
  .hero-controls { position: absolute; left: 477px; top: 235px; display: flex; gap: 2px; }
  .hero-controls span { width: 29px; height: 29px; background: var(--red); display: flex; align-items: center; justify-content: center; }

  .welcome { position: absolute; top: 363px; left: 0; width: 861px; height: 217px; background: var(--red); color: var(--white); text-align: center; }
  .welcome h1 { font-size: 14.5px; margin-top: 25px; margin-bottom: 15px; }
  .welcome p { width: 560px; margin: 0 auto 14.5px; font-size: 7.3px; line-height: 14.8px; }

  .features { position: absolute; top: 613px; left: 133px; display: flex; gap: 32px; }
  .feature { width: 177px; height: 251px; text-align: center; border: 1px solid var(--card-border); background: var(--card-light); padding-top: 34px; }
  .feature h2 { font-size: 13px; color: var(--red); margin-bottom: 14px; }
  .feature p { font-size: 7.3px; line-height: 14.6px; color: var(--muted); padding: 0 18px; }
  .feature.active { background: var(--card-dark); border-color: var(--card-dark); }
  .feature.active h2, .feature.active p { color: var(--white); }
  .feature-art { height: 70px; margin: 0 auto 16px; display: flex; align-items: center; justify-content: center; }
  .people-placeholder { width: 88px; height: 64px; background: linear-gradient(180deg, #8a8a8a, #7a7a7a); border-radius: 3px; }
  .feature .link { color: var(--red); font-style: italic; }

  .about { position: absolute; top: 901px; left: 0; width: 861px; height: 237px; background: var(--band-grey); padding: 0 124px; }
  .about h2 { font-size: 11.5px; color: var(--red); margin: 32px 0 10px; }
  .about h2 + p { margin-top: 0; }
  .about h2.second { margin-top: 19px; }
  .about p { font-size: 7.3px; line-height: 14.6px; color: var(--muted); margin-bottom: 14.5px; }

  .site-footer { position: absolute; top: 1138px; left: 0; width: 861px; height: 62px; background: var(--footer); color: var(--footer-text); font-size: 7.3px; }
  .footer-nav { position: absolute; left: 124px; top: 17px; display: flex; gap: 23px; }
  .copyright { position: absolute; left: 124px; top: 35px; }
  .social { position: absolute; left: 612px; top: 18px; display: flex; gap: 6px; }
  .social span { width: 20px; height: 20px; border-radius: 50%; background: #7a7a7a; }
</style>
</head>
<body>
  <header class="site-header">
    <div class="brand"><span class="brand-dot"></span><span class="brand-name">ClueVane</span></div>
    <nav class="main-nav"><span class="caret">Register</span><span class="caret">Sign in</span><span>About Us</span></nav>
  </header>

  <section class="hero" role="img" aria-label="Black and white photo of an investigator with a magnifying glass inside a tunnel of binary digits">
    <div class="hero-caption one heading">Clue Vane, track, relate, investigate, solve!</div>
    <div class="hero-caption two heading">Basic Clue Vane will allow any registered user to create</div>
    <div class="hero-controls">
      <span><svg width="10" height="14" viewBox="0 0 10 14"><path d="M8 1 2 7l6 6" fill="none" stroke="#fff" stroke-width="1.6"/></svg></span>
      <span><svg width="10" height="14" viewBox="0 0 10 14"><path d="M2 1l6 6-6 6" fill="none" stroke="#fff" stroke-width="1.6"/></svg></span>
    </div>
  </section>

  <section class="welcome">
    <h1 class="heading">Welcome to Clue Vane</h1>
    <p>Have you ever compiled a lot of data about something, but been unable to figure out what it means? Often, the number of people involved, the number of events at which they might have met, and the number of common contacts are just too much for a person to track. This can happen when you are trying to understand the players and interests in current events, or the characters and actions in a novel. It’s easy to collect the data, but hard to visualize it or analyze the relationships.</p>
    <p>This is where ClueVane comes in. ClueVane allows you to easily visualize people, events, things, groups, and timelines and to easily see the relationships between them.</p>
    <p>Use ClueVane to plot a novel, or to investigate a crime. Use it to analyze your favorite conspiracy theory and look for relationships that have eluded the investigators. Use it to track the causes and results of historical events – or current ones. Use it to track changing relationships among your friends at high school. Use it to track the twists and turns of a role-playing game. There’s no end to what you can investigate with ClueVane</p>
  </section>

  <section class="features">
    <article class="feature active">
      <h2 class="heading">Organize</h2>
      <div class="feature-art"><div class="people-placeholder" role="img" aria-label="Illustration of two seated people joined by a plus sign"></div></div>
      <p>ClueVane is an on-line system that allows you to enter what you know about a person, event, object, or group. Who are their friends – and who are their enemies?</p>
    </article>
    <article class="feature">
      <h2 class="heading">Vistualize</h2>
      <div class="feature-art">
        <svg width="94" height="54" viewBox="0 0 94 54" aria-hidden="true">
          <rect x="12" y="2" width="70" height="44" rx="2" fill="none" stroke="#7a7a7a" stroke-width="3"/>
          <path d="M0 49h94l-3 4H3z" fill="#7a7a7a"/>
        </svg>
      </div>
      <p>Once data has been entered, use ClueVane’s graphical analysis tools to analyze your data in new ways.</p>
    </article>
    <article class="feature">
      <h2 class="heading">Colaborate</h2>
      <div class="feature-art">
        <svg width="76" height="66" viewBox="0 0 76 66" aria-hidden="true">
          <path d="M14 30a24 24 0 0 1 42-15l-7 7h20V2l-6 6A34 34 0 0 0 4 30z" fill="#6b6b6b"/>
          <path d="M62 36a24 24 0 0 1-42 15l7-7H7v20l6-6a34 34 0 0 0 59-22z" fill="#6b6b6b"/>
        </svg>
      </div>
      <p>ClueVane is an on-line system that allows you to enter what you know about a person, event, object, or group. Who are their friends. <span class="link">Join with others</span></p>
    </article>
  </section>

  <section class="about">
    <h2 class="heading">How does ClueVane work?</h2>
    <p>Once data has been entered, use ClueVane’s graphical analysis tools to analyze your data in new ways. Use relationship maps to find out how two people or groups are associated. Use timeline analysis to show cause and effect of seemingly unrelated events. Use social network mapping to show how relationships change over time. Look for events that stand out or relationships that have great impact on multiple events. Like a spider’s web, look for the intersections that matter, then look for the players that brought that intersection into focus.</p>
    <h2 class="heading second">What do I get with ClueVane?</h2>
    <p>Basic ClueVane will allow any registered user to create, maintain and analyze one investigation. Advanced features will be available a la carte and will include special analytical reports, multiple investigations, and the ability to share an investigation among multiple users. Investigations of general interest could also be shared publicly in read-only mode.</p>
    <p>You will also get access to several read-only public investigations to use as a model. These might include the plots of popular novels or movies, the details of a major political event, or an investigation into a famous crime.</p>
  </section>

  <footer class="site-footer">
    <nav class="footer-nav"><span>Home</span><span>About Us</span><span>Register</span><span>Sign In</span></nav>
    <div class="copyright">Copyright 2014, Clue Vane. All rights reserved.</div>
    <div class="social" aria-label="Social links"><span></span><span></span><span></span><span></span><span></span></div>
  </footer>
</body>
</html>
```